there are a couple things we are trying to rebrand our shop with a new logo, the current Logo I am attaching we want to have something new and refreshing with a hint of fashion with a simple logo that is easy to remember, the name of the company is Brindle Tee Wholesale, our website is brindletee.com we also have a retail store that the window graphics needs to be completely redone as pictured. the sign on top will also need to be redone keep in mind we are a wholesale shop so we can to attract customers that are driving easily, the window measurements are 9 windows, window #8 should tell the customers to use the other door because there is no entrance from here
all sizes below are the width of the window
1. 37
2. 30
3. 37
4. 36
5. 30
6. 42
7. 30
8. 30
9. 30

```html
<!DOCTYPE html>
<html lang="en">
<head>
<meta charset="utf-8">
<title>Brindle Tee Wholesale – Storefront Sign and Window Graphics</title>
<link href="https://fonts.googleapis.com/css2?family=Oswald:wght@500;600;700&display=swap" rel="stylesheet">
<style>
  :root {
    --navy: #2a2c62;
    --navy-light: #444a9c;
    --navy-dark: #1f2152;
    --red: #e3282f;
    --red-dark: #b81d23;
    --white: #ffffff;
    --off-white: #f3f3f5;
    --charcoal: #1e1e23;
    --strip: #8d8d8f;
    --bg-top: #858587;
    --bg-bottom: #c4c4c6;
  }
  * { box-sizing: border-box; margin: 0; padding: 0; }
  html, body { width: 1200px; height: 1117px; overflow: hidden; }
  body { font-family: "Oswald", "Arial Narrow", sans-serif; }

  .canvas {
    position: relative;
    width: 1200px;
    height: 1117px;
    background: linear-gradient(180deg, var(--bg-top) 0%, var(--bg-bottom) 100%);
  }

  .storefront-sign {
    position: absolute;
    left: 55px;
    top: 418px;
    width: 1090px;
    height: 112px;
  }
  .storefront-sign text {
    font-family: "Oswald", "Arial Narrow", sans-serif;
    font-weight: 700;
    font-size: 100px;
  }
  .sign-word-wholesale { fill: var(--white); }
  .sign-word-shirts { fill: var(--navy); }
  .sign-word-caps { fill: var(--red); }

  .window-strip {
    position: absolute;
    left: 52px;
    top: 548px;
    width: 1096px;
    height: 134px;
    padding: 8px;
    background: var(--strip);
    display: flex;
    gap: 8px;
  }

  .window-panel {
    position: relative;
    flex: 1;
    background: var(--white);
    overflow: hidden;
  }

  .brand-tag {
    position: absolute;
    top: 5px;
    left: 5px;
    display: flex;
    align-items: center;
    gap: 3px;
    z-index: 2;
  }
  .brand-mark {
    width: 6px;
    height: 6px;
    background: var(--red);
  }
  .brand-name {
    font-size: 8px;
    font-weight: 600;
    color: var(--red);
    line-height: 1;
    letter-spacing: 0.2px;
  }

  .product-photo {
    position: absolute;
    top: 4px;
    left: 22%;
    width: 62%;
    height: 82px;
    border-radius: 4px 4px 0 0;
  }
  .photo-tee { background: linear-gradient(180deg, #5b5d5f, #3f4143); }
  .photo-cap { background: linear-gradient(180deg, #d9cdb3 0%, #2b2f3e 55%, #1d2030 100%); }
  .photo-women { background: linear-gradient(180deg, #e9d9c4, #d8c3a5); }
  .photo-joggers { background: linear-gradient(180deg, #2a2a2c, #111113); }
  .photo-varsity { background: linear-gradient(180deg, #3a3a3d, #1b1b1e); }
  .photo-hoodie { background: linear-gradient(180deg, #a9a9ac, #848487); }
  .photo-youth { background: linear-gradient(180deg, #8a2a34, #6b1d26); }
  .photo-tracksuit { background: linear-gradient(180deg, #e6e4e0, #c9c7c2); }

  .label-band {
    position: absolute;
    left: 0;
    right: 0;
    bottom: 0;
    height: 32px;
  }
  .label-band-shadow {
    position: absolute;
    inset: 0;
    background: var(--charcoal);
    clip-path: polygon(0 22%, 100% 0, 100% 100%, 0 100%);
  }
  .label-band-fill {
    position: absolute;
    inset: 0;
    background: var(--red);
    clip-path: polygon(0 10%, 100% 34%, 100% 100%, 0 100%);
  }
  .label-text {
    position: absolute;
    left: 0;
    right: 0;
    bottom: 6px;
    text-align: center;
    color: var(--white);
    font-size: 10.5px;
    font-weight: 500;
    text-transform: uppercase;
    letter-spacing: 0.1px;
    white-space: nowrap;
  }

  .window-panel--notice { background: var(--charcoal); }
  .notice-card {
    position: absolute;
    top: 6px;
    left: 5px;
    right: 5px;
    height: 102px;
    background: linear-gradient(160deg, #ee3037, var(--red-dark));
    transform: skewY(4deg);
    display: flex;
    flex-direction: column;
    justify-content: center;
    padding-left: 18px;
  }
  .notice-line {
    color: var(--white);
    font-size: 24px;
    font-weight: 600;
    line-height: 0.98;
    text-transform: uppercase;
    display: flex;
    align-items: center;
    gap: 3px;
    transform: skewY(-4deg);
  }
  .notice-arrow { width: 22px; height: 14px; }
</style>
</head>
<body>
<main class="canvas">

  <svg class="storefront-sign" viewBox="0 0 1090 112" aria-label="Wholesale T-Shirts / Caps">
    <defs>
      <linearGradient id="signNavy" x1="0" y1="0" x2="1" y2="0">
        <stop offset="0" stop-color="var(--navy-dark)"/>
        <stop offset="0.55" stop-color="var(--navy-light)"/>
        <stop offset="1" stop-color="var(--navy)"/>
      </linearGradient>
      <linearGradient id="signWhite" x1="0" y1="0" x2="0" y2="1">
        <stop offset="0" stop-color="#e4e4e8"/>
        <stop offset="0.12" stop-color="var(--white)"/>
        <stop offset="1" stop-color="var(--off-white)"/>
      </linearGradient>
    </defs>
    <polygon points="0,0 480,0 440,112 0,112" fill="url(#signNavy)"/>
    <polygon points="480,0 1090,0 1090,112 440,112" fill="url(#signWhite)"/>
    <polygon points="1090,4 1050,112 1090,112" fill="var(--red)"/>
    <g transform="skewX(-9)">
      <text class="sign-word-wholesale" x="42" y="92" textLength="390" lengthAdjust="spacingAndGlyphs">WHOLESALE</text>
      <text class="sign-word-shirts" x="512" y="92" textLength="300" lengthAdjust="spacingAndGlyphs">T-SHIRTS</text>
      <text class="sign-word-caps" x="830" y="92" textLength="215" lengthAdjust="spacingAndGlyphs">/ CAPS</text>
    </g>
  </svg>

  <section class="window-strip" aria-label="Window graphics">
    <article class="window-panel">
      <div class="brand-tag"><span class="brand-mark"></span><span class="brand-name">Brindle Tee</span></div>
      <div class="product-photo photo-tee" role="img" aria-label="Model wearing a charcoal crew-neck t-shirt"></div>
      <div class="label-band"><span class="label-band-shadow"></span><span class="label-band-fill"></span><span class="label-text">Men's Collections</span></div>
    </article>

    <article class="window-panel">
      <div class="brand-tag"><span class="brand-mark"></span><span class="brand-name">Brindle Tee</span></div>
      <div class="product-photo photo-cap" role="img" aria-label="Navy snapback caps stacked"></div>
      <div class="label-band"><span class="label-band-shadow"></span><span class="label-band-fill"></span><span class="label-text">Headwear Collection</span></div>
    </article>

    <article class="window-panel">
      <div class="brand-tag"><span class="brand-mark"></span><span class="brand-name">Brindle Tee</span></div>
      <div class="product-photo photo-women" role="img" aria-label="Model wearing a cream cropped hoodie"></div>
      <div class="label-band"><span class="label-band-shadow"></span><span class="label-band-fill"></span><span class="label-text">Women's Collections</span></div>
    </article>

    <article class="window-panel">
      <div class="brand-tag"><span class="brand-mark"></span><span class="brand-name">Brindle Tee</span></div>
      <div class="product-photo photo-joggers" role="img" aria-label="Model wearing black joggers"></div>
      <div class="label-band"><span class="label-band-shadow"></span><span class="label-band-fill"></span><span class="label-text">Joggers Collection</span></div>
    </article>

    <article class="window-panel">
      <div class="brand-tag"><span class="brand-mark"></span><span class="brand-name">Brindle Tee</span></div>
      <div class="product-photo photo-varsity" role="img" aria-label="Model wearing a black satin varsity jacket"></div>
      <div class="label-band"><span class="label-band-shadow"></span><span class="label-band-fill"></span><span class="label-text">Varsity Jacket</span></div>
    </article>

    <article class="window-panel">
      <div class="brand-tag"><span class="brand-mark"></span><span class="brand-name">Brindle Tee</span></div>
      <div class="product-photo photo-hoodie" role="img" aria-label="Model wearing a heather grey hoodie"></div>
      <div class="label-band"><span class="label-band-shadow"></span><span class="label-band-fill"></span><span class="label-text">Hoodies Collection</span></div>
    </article>

    <article class="window-panel">
      <div class="brand-tag"><span class="brand-mark"></span><span class="brand-name">Brindle Tee</span></div>
      <div class="product-photo photo-youth" role="img" aria-label="Child wearing a maroon t-shirt"></div>
      <div class="label-band"><span class="label-band-shadow"></span><span class="label-band-fill"></span><span class="label-text">Youth Collection</span></div>
    </article>

    <article class="window-panel window-panel--notice">
      <div class="notice-card">
        <span class="notice-line">Use
          <svg class="notice-arrow" viewBox="0 0 22 14" aria-hidden="true">
            <path d="M1 7 H15" stroke="var(--white)" stroke-width="3"/>
            <polygon points="13,1 21,7 13,13" fill="var(--white)"/>
          </svg>
        </span>
        <span class="notice-line">Other</span>
        <span class="notice-line">Door</span>
      </div>
    </article>

    <article class="window-panel">
      <div class="brand-tag"><span class="brand-mark"></span><span class="brand-name">Brindle Tee</span></div>
      <div class="product-photo photo-tracksuit" role="img" aria-label="Model wearing a light grey track suit"></div>
      <div class="label-band"><span class="label-band-shadow"></span><span class="label-band-fill"></span><span class="label-text">Track Suits</span></div>
    </article>
  </section>

</main>
</body>
</html>
```